依頼詳細
■素材
商品ロゴや写真の素材を添付します。
使う文言や表などもありますので、レイアウトとデザインをお願い致します。

■色味やイメージについて
色合いやイメージのこだわりはありませんので、写真や文字を上手に配置して頂き、気に入ったデザインの方を当選としたいと思います。
なお、文字は特殊なフォントはなるべく使わないようお願いします。

■提出データ
当選者の方は、.ai 及び、.psdファイルでの提出をお願いいたします。

■その他
なお、少しでも多くの方にお支払できるよう、当選者の方以外に、参加報酬を5名様にお支払いします。
不明な点等ございましたら、お気軽にお問合せ下さい。
記載項目
■表面
・キャッチコピー:
「作業道仕上げを早く、美しく、より強固に!」

・商品ロゴ:

```html
<!DOCTYPE html>
<html lang="ja">
<head>
<meta charset="UTF-8">
<title>作業道仕上げ アタッチメント</title>
<link rel="stylesheet" href="https://fonts.googleapis.com/css2?family=Noto+Sans+JP:wght@700;900&display=swap">
<style>
  :root {
    --paper: #ffffff;
    --yellow: #f7ef4d;
    --ink: #111111;
    --red: #e0141e;
    --label-bg: rgba(20, 20, 20, 0.72);
    --label-ink: #ffffff;
    --photo-top: #a7b3ba;
    --photo-mid: #8a7a5e;
    --photo-bottom: #5f4d37;
  }
  * { margin: 0; padding: 0; box-sizing: border-box; }
  html, body { width: 878px; height: 1200px; overflow: hidden; background: var(--paper); }
  .flyer {
    position: relative;
    width: 878px;
    height: 1200px;
    background: var(--paper);
    padding: 10px;
    font-family: "Noto Sans JP", sans-serif;
    color: var(--ink);
  }
  .flyer__sheet {
    position: relative;
    width: 100%;
    height: 100%;
    background: var(--yellow);
    overflow: hidden;
  }
  .photo-column {
    position: absolute;
    left: 283px;
    top: 48px;
    width: 307px;
    display: flex;
    flex-direction: column;
    gap: 10px;
  }
  .work-photo {
    position: relative;
    height: 214px;
    background: linear-gradient(180deg, var(--photo-top) 0%, var(--photo-mid) 55%, var(--photo-bottom) 100%);
  }
  .work-photo__label {
    position: absolute;
    top: 0;
    left: 50%;
    transform: translateX(-50%);
    background: var(--label-bg);
    color: var(--label-ink);
    font-size: 17px;
    font-weight: 700;
    padding: 2px 14px;
    white-space: nowrap;
  }
  .vertical {
    position: absolute;
    writing-mode: vertical-rl;
    font-weight: 900;
    line-height: 1;
    white-space: nowrap;
  }
  .headline { margin: 0; }
  .headline__lead {
    left: 765px;
    top: 60px;
    font-size: 40px;
  }
  .headline__accent {
    color: var(--red);
    -webkit-text-stroke: 4px var(--ink);
    paint-order: stroke fill;
  }
  .headline__fast {
    left: 743px;
    top: 348px;
    font-size: 84px;
  }
  .headline__beautiful {
    left: 610px;
    top: 250px;
    font-size: 96px;
  }
  .headline__more {
    left: 638px;
    top: 650px;
    font-size: 40px;
  }
  .headline__strong {
    left: 609px;
    top: 740px;
    font-size: 98px;
  }
  .lead-left {
    left: 210px;
    top: 48px;
    font-size: 40px;
  }
  .feature {
    left: 112px;
    top: 130px;
    font-size: 52px;
  }
  .feature__number {
    font-size: 78px;
    color: var(--red);
    text-combine-upright: all;
  }
  .brand {
    position: absolute;
    left: 22px;
    bottom: 26px;
    display: flex;
    align-items: center;
    gap: 6px;
    font-size: 15px;
    font-weight: 900;
    color: var(--red);
  }
  .brand__mark {
    width: 20px;
    height: 20px;
    background: var(--red);
  }
</style>
</head>
<body>
<div class="flyer">
  <div class="flyer__sheet">
    <div class="photo-column">
      <div class="work-photo" role="img" aria-label="掘削機で作業道を通常転圧している写真"><span class="work-photo__label">通常の転圧</span></div>
      <div class="work-photo" role="img" aria-label="掘削機で下面から転圧している写真"><span class="work-photo__label">下面からの転圧</span></div>
      <div class="work-photo" role="img" aria-label="掘削機で法面を仕上げている写真"><span class="work-photo__label">法面仕上げ</span></div>
      <div class="work-photo" role="img" aria-label="掘削機で切土を成形している写真"><span class="work-photo__label">切土成形</span></div>
      <div class="work-photo" role="img" aria-label="掘削機で溝切りをしている写真"><span class="work-photo__label">溝切り</span></div>
    </div>

    <h1 class="headline">
      <span class="vertical headline__lead">作業道仕上げを</span>
      <span class="vertical headline__accent headline__fast">早く、</span>
      <span class="vertical headline__accent headline__beautiful">美しく、</span>
      <span class="vertical headline__more">より</span>
      <span class="vertical headline__accent headline__strong">強固に！</span>
    </h1>

    <p class="vertical lead-left">道作りの常識を変える！</p>
    <p class="vertical feature">着脱わずか<span class="feature__number">5</span>秒で、様々な作業が可能に！</p>

    <div class="brand"><span class="brand__mark"></span><span class="brand__name">TERRA GRIP</span></div>
  </div>
</div>
</body>
</html>
```